Web App Dashboard Design for Healthcare Company

We have developed a simple web application with 3 navigation menus. We like the current design (very much modeled after Ledgerly), but we want to explore UI options for the branding, header, menus, and footer that we may not have considered.

The attached screenshots show the layout and two menu "hover" views as they currently exist.

This web application is used by employees only.

Menu 1 - Module Menu:
Allows the user to switch easily between Account, Employee, and Care Management.

Menu 2 - Reports Menu
Allows user to view available reports within each Module.

Menu 3 - Admin Menu
Allows the user to easily create new content types within each module.

Use our branded colors and font.

Colors:
Logo Blue (dark): 00c0f3
Logo Blue (light): 44c8f5
Nav Blue: 0994d0
Green: 71b44b
Grayscale: (not specified)

Font:
Lato (Google Font)

Target Market(s)

Internal staff.

Industry/Entity Type

Healthcare

Number of Pages Required

3 page

Font styles to use
Sans Serif
Other font styles liked:
• Lato (Google Font)

Colors
0293ce
9bcb3c

Requirements
Must have
• It's really a one page design, but we want to see the two "hover" views for the Module Menu and the Admin Menu.
• It should also be very clear which "Report" page the user is on (the active menu link).
• Must use branded colors, font, and logo.
• Logo Blue (dark): 00c0f3
• Logo Blue (light): 44c8f5
• Nav Blue: 0994d0
• Green: 71b44b
• Grayscale: Designer may choose
Nice to have
• It would be nice to have simple uncluttered payouts.
Should not have
• The design should not have menu options exposed by default.

```html
<!DOCTYPE html>
<html lang="en">
<head>
<meta charset="utf-8">
<title>CareLoop – Reports</title>
<link href="https://fonts.googleapis.com/css2?family=Lato:wght@400;700&display=swap" rel="stylesheet">
<style>
  :root {
    --green: #71b44b;
    --nav-sky: #6ec6ee;
    --link-blue: #44c8f5;
    --logo-blue: #00c0f3;
    --ink: #333333;
    --rule: #555555;
    --rule-soft: #dddddd;
    --white: #ffffff;
  }
  * { box-sizing: border-box; margin: 0; padding: 0; }
  html, body { width: 1200px; height: 813px; overflow: hidden; background: var(--white); }
  body { font-family: "Lato", sans-serif; color: var(--ink); position: relative; }

  .top-bar {
    position: absolute; top: 0; left: 0; width: 1200px; height: 55px;
    background: var(--green); color: var(--white);
    display: flex; align-items: center; justify-content: space-between;
    padding: 0 66px 0 67px; font-size: 16px; letter-spacing: .2px;
  }
  .top-bar .item { display: flex; align-items: center; gap: 8px; }
  .top-bar .user-links { display: flex; gap: 24px; }
  .top-bar svg { width: 18px; height: 18px; }

  .brand {
    position: absolute; top: 86px; left: 0; width: 1200px;
    display: flex; justify-content: center; align-items: center; gap: 10px;
  }
  .brand-mark { width: 22px; height: 22px; background: var(--logo-blue); }
  .brand-name { font-size: 34px; font-weight: 700; color: var(--ink); }

  .module-select {
    position: absolute; top: 190px; left: 459px; width: 282px; height: 30px;
    border: 1px solid var(--ink); display: flex; align-items: center;
    justify-content: space-between; padding: 0 16px 0 16px; font-size: 16px;
  }
  .module-select .caret {
    width: 0; height: 0; border-left: 6px solid transparent;
    border-right: 6px solid transparent; border-top: 7px solid var(--ink);
  }

  .main-nav {
    position: absolute; top: 249px; left: 0; width: 1200px; height: 55px;
    background: var(--nav-sky);
  }
  .main-nav a {
    position: absolute; top: 0; height: 55px; line-height: 55px;
    color: var(--white); text-decoration: none; font-size: 16px; letter-spacing: .3px;
  }
  .main-nav a.active { background: var(--green); width: 110px; text-align: center; }

  .report-table {
    position: absolute; top: 339px; left: 137px; width: 926px; height: 368px;
    border: 1px solid var(--rule); border-collapse: collapse; table-layout: fixed;
    font-size: 14px;
  }
  .report-table th, .report-table td {
    border-left: 1px solid var(--rule-soft); text-align: center; font-weight: 400;
  }
  .report-table th:first-child, .report-table td:first-child { border-left: none; }
  .report-table thead tr { height: 39px; border-bottom: 1px solid var(--rule-soft); }
  .report-table th { padding-top: 6px; }
  .report-table tbody tr { height: 52px; }
  .report-table tbody tr:first-child td { padding-top: 6px; }
  .report-table .view-link { color: var(--link-blue); text-decoration: underline; }

  .pagination {
    position: absolute; top: 720px; right: 137px;
    display: flex; align-items: center; gap: 8px; font-size: 14px;
  }
  .pagination .label { margin-right: 6px; }
  .pagination .page {
    border: 1px solid var(--ink); min-width: 19px; height: 19px;
    font-size: 12px; display: flex; align-items: center; justify-content: center; padding: 0 2px;
  }
  .pagination .gap { letter-spacing: 1px; font-size: 10px; }

  .site-footer {
    position: absolute; top: 765px; left: 0; width: 1200px; height: 48px;
    background: var(--green); color: var(--white);
    display: flex; align-items: center; justify-content: space-between;
    padding: 0 16px 0 82px; font-size: 15px;
  }
  .site-footer .right { display: flex; align-items: center; gap: 50px; }
  .site-footer .contact { display: flex; align-items: center; gap: 9px; }
  .site-footer svg { width: 18px; height: 18px; }
</style>
</head>
<body>
  <header class="top-bar">
    <div class="item">
      <svg viewBox="0 0 18 18" aria-hidden="true"><rect x="1.5" y="1.5" width="15" height="15" rx="2" fill="none" stroke="#fff" stroke-width="1.6"/><path d="M9 5v8M5 9h8" stroke="#fff" stroke-width="1.6"/></svg>
      <span>REPORTS</span>
    </div>
    <div class="user-links">
      <div class="item">
        <svg viewBox="0 0 18 18" aria-hidden="true"><circle cx="9" cy="9" r="8.5" fill="#fff"/><rect x="8" y="7.5" width="2" height="6" fill="#71b44b"/><circle cx="9" cy="5" r="1.2" fill="#71b44b"/></svg>
        <span>MY INFO</span>
      </div>
      <div class="item">
        <svg viewBox="0 0 18 18" aria-hidden="true"><path d="M8 2H3a1.5 1.5 0 0 0-1.5 1.5v11A1.5 1.5 0 0 0 3 16h5" fill="none" stroke="#fff" stroke-width="2"/><path d="M7 7h5V4l5 5-5 5v-3H7z" fill="#fff"/></svg>
        <span>LOG OUT</span>
      </div>
    </div>
  </header>

  <div class="brand">
    <span class="brand-mark"></span>
    <span class="brand-name">CareLoop</span>
  </div>

  <div class="module-select">
    <span>Account Management</span>
    <span class="caret"></span>
  </div>

  <nav class="main-nav">
    <a style="left:87px">REMINDERS</a>
    <a style="left:272px">ADMIN</a>
    <a style="left:392px">PATIENT REQUEST</a>
    <a class="active" style="left:590px">REPORTS</a>
    <a style="left:758px">MY COMPANY</a>
  </nav>

  <table class="report-table">
    <colgroup>
      <col style="width:112px"><col style="width:101px"><col style="width:97px">
      <col style="width:113px"><col style="width:100px"><col style="width:101px">
      <col style="width:97px"><col style="width:113px"><col style="width:92px">
    </colgroup>
    <thead>
      <tr><th>Name</th><th>Data</th><th>Date</th><th>Care</th><th></th><th></th><th></th><th></th><th></th></tr>
    </thead>
    <tbody>
      <tr><td>JOHN</td><td>Info</td><td>15-03-17</td><td>Data</td><td>Data1</td><td>Data2</td><td>Task2</td><td>Task3</td><td><span class="view-link">View</span></td></tr>
      <tr><td>JOHN</td><td>Info</td><td>15-03-17</td><td>Data</td><td>Data1</td><td>Data2</td><td>Task2</td><td>Task3</td><td><span class="view-link">View</span></td></tr>
      <tr><td>JOHN</td><td>Info</td><td>15-03-17</td><td>Data</td><td>Data1</td><td>Data2</td><td>Task2</td><td>Task3</td><td><span class="view-link">View</span></td></tr>
      <tr><td>JOHN</td><td>Info</td><td>15-03-17</td><td>Data</td><td>Data1</td><td>Data2</td><td>Task2</td><td>Task3</td><td><span class="view-link">View</span></td></tr>
      <tr><td>JOHN</td><td>Info</td><td>15-03-17</td><td>Data</td><td>Data1</td><td>Data2</td><td>Task2</td><td>Task3</td><td><span class="view-link">View</span></td></tr>
      <tr><td>JOHN</td><td>Info</td><td>15-03-17</td><td>Data</td><td>Data1</td><td>Data2</td><td>Task2</td><td>Task3</td><td><span class="view-link">View</span></td></tr>
    </tbody>
  </table>

  <div class="pagination">
    <span class="label">Page</span>
    <span class="page">1</span>
    <span class="page">2</span>
    <span class="gap">...........</span>
    <span class="page">10</span>
  </div>

  <footer class="site-footer">
    <span>© 2017 CARELOOP. ALL RIGHTS RESERVED.</span>
    <div class="right">
      <div class="contact">
        <svg viewBox="0 0 18 18" aria-hidden="true"><rect width="18" height="18" rx="3" fill="#fff"/><path d="M5.5 4c.6-.4 1.2-.3 1.5.2l1 1.8c.3.5.1 1-.3 1.3l-.6.5c.5 1.2 1.4 2.1 2.6 2.7l.5-.6c.3-.4.9-.5 1.3-.2l1.8 1c.5.3.6 1 .2 1.5-.8 1-2 1.3-3.2.7C7.8 11.8 5.9 10 4.9 7.6 4.4 6.2 4.6 4.8 5.5 4z" fill="#71b44b"/></svg>
        <span>CONTACT US</span>
      </div>
      <span>C12</span>
    </div>
  </footer>
</body>
</html>
```